8" x 11" One Page Flyer for Fence Installation Company

We are looking to promote our business with a new flyer that would be handed out in person to people or put at their mailbox/door at their homes. The flyer needs to be creative and attention-grabbing. I have attached some of our previous flyers and our website information. Do not call or email regarding the flyer. We want the flyer to look professional but also friendly. One page, NOT folded. You can use images from our website at www.MyBraxtonYard.com or our Facebook page at www.Facebook.com/HollowbrookRailsBKT. We are flexible with what photos you can use but there must be photos of OUR fences on the flyer. More photos specifically can also be provided. Colors need to be suitable for a flyer printed on canary yellow in color paper OR white paper.

Target Market(s)

Homeowners that need a new fence

Industry/Entity Type

Construction

Font styles to use
Sans Serif
Other font styles liked:
• HD Colton

Colors
0054AA
0677BA
7BADD7
CADEEF
E8F1F8
0094D4
00A9DD
6FCCEA
C7EBF8
E9F6FB

Requirements
Must have
• Our fence photos - mostly wood fence photos (different designs), SIZE SHOULD BE LETTER SIZE 8" x 11"
Nice to have
• A nice bible verse featured at the bottom of the flyer.
Should not have
• DO NOT COPY THE WEBSITE FORMAT, I WANT SOMETHING UNIQUE. Other people's fence photos, they must all come from our website or facebook page

```html
<!DOCTYPE html>
<html lang="en">
<head>
<meta charset="utf-8">
<title>Hollowbrook Rails Flyer</title>
<link rel="stylesheet" href="https://fonts.googleapis.com/css2?family=Exo+2:wght@600;700;800;900&family=Montserrat:wght@400;500;600;700&display=swap">
<style>
:root{
  --backdrop:#7a7a7a;
  --orange:#f7941d;
  --blue:#3f7fcc;
  --blue-light:#4b93d6;
  --brown:#553a28;
  --white:#ffffff;
  --logo-panel:#ececea;
  --logo-blue:#3a86c8;
  --ink:#2b2119;
}
*{margin:0;padding:0;box-sizing:border-box}
html,body{width:1200px;height:1200px;overflow:hidden;background:var(--backdrop)}
.flyer{
  position:absolute;left:229px;top:94px;width:1194px;height:1628px;
  transform:scale(0.6211);transform-origin:0 0;overflow:hidden;
  font-family:"Montserrat",sans-serif;color:var(--white);
  box-shadow:12px 14px 18px rgba(0,0,0,.35);
}
.shapes{position:absolute;inset:0;width:1194px;height:1628px}
.abs{position:absolute}
.brand-name{left:163px;top:48px;font-family:"Exo 2",sans-serif;font-weight:700;font-size:23px;color:var(--logo-blue);white-space:nowrap}
.brand-phone{left:163px;top:76px;font-family:"Exo 2",sans-serif;font-weight:700;font-size:21px;color:var(--ink);letter-spacing:.5px}
.brand-tag{left:163px;top:104px;font-weight:600;font-size:7.5px;color:var(--ink)}
.headline{left:60px;top:232px;font-family:"Exo 2",sans-serif;font-weight:700;font-size:124px;line-height:112px;color:var(--orange);letter-spacing:-1px}
.subhead{left:60px;top:468px;font-weight:400;font-size:60px;line-height:68px;letter-spacing:1px}
.why{left:644px;top:872px;font-family:"Exo 2",sans-serif;font-weight:900;font-size:50px;line-height:48px}
.why span{color:var(--orange);display:block}
.why-rule{left:645px;top:978px;width:87px;height:3px;background:var(--white)}
.why-lead{left:644px;top:990px;font-weight:600;font-size:29px;line-height:34px;width:520px}
.perks{left:674px;top:1088px;list-style:none;font-size:20px;line-height:36.3px}
.perks li{position:relative;padding-left:30px}
.perks svg{position:absolute;left:0;top:8px;width:20px;height:20px}
.where{left:58px;top:1440px;font-weight:700;font-size:31px;letter-spacing:1px}
.address{left:384px;top:1430px;font-size:20px;line-height:24px}
.showroom{left:664px;top:1444px;font-weight:700;font-size:22px}
.web{left:76px;top:1543px;font-weight:700;font-size:23px;letter-spacing:4.4px;color:#111}
.hours{left:661px;top:1516px;width:490px;font-size:19.5px;line-height:24px;font-weight:400}
.hours b{font-weight:600}
</style>
</head>
<body>
<div class="flyer">
  <svg class="shapes" viewBox="0 0 1194 1628" aria-hidden="false">
    <defs>
      <linearGradient id="yard" x1="0" y1="0" x2="1" y2="1">
        <stop offset="0" stop-color="#3b3a22"/>
        <stop offset=".45" stop-color="#4d3a28"/>
        <stop offset=".75" stop-color="#8a6a45"/>
        <stop offset="1" stop-color="#b08a5c"/>
      </linearGradient>
      <linearGradient id="panel" x1="0" y1="0" x2="0" y2="1">
        <stop offset="0" stop-color="#3c72c4"/>
        <stop offset="1" stop-color="#4b93d6"/>
      </linearGradient>
    </defs>
    <rect width="1194" height="1000" fill="url(#yard)" role="img" aria-label="Backyard lined with a tall wooden privacy fence, shrubs and flowering roses"/>
    <polygon points="62,0 406,0 406,165 62,203" fill="var(--logo-panel)"/>
    <circle cx="125" cy="70" r="13" fill="var(--orange)"/>
    <polygon points="0,928 598,782 598,802 0,948" fill="var(--blue)"/>
    <polygon points="0,948 598,802 598,1412 0,1412" fill="var(--white)"/>
    <polygon points="598,780 1194,925 1194,1412 598,1412" fill="url(#panel)"/>
    <polygon points="58,808 306,750 306,908 58,966" fill="var(--white)"/>
    <polygon points="62,813 301,758 301,903 62,958" fill="#5f7a3a" role="img" aria-label="Black aluminium fence around a lawn"/>
    <polygon points="320,744 568,682 568,838 320,898" fill="var(--white)"/>
    <polygon points="324,748 564,688 564,833 324,893" fill="#c9a56e" role="img" aria-label="Wooden picket fence with a gate beside a house"/>
    <polygon points="63,969 562,853 562,1092 63,1092" fill="var(--white)"/>
    <polygon points="67,973 558,858 558,1088 67,1088" fill="#9c8760" role="img" aria-label="Long four-rail wooden ranch fence along a field"/>
    <rect x="66" y="1108" width="491" height="287" fill="#eceef1" stroke="var(--orange)" stroke-width="3" role="img" aria-label="Street map showing the showroom location"/>
    <rect x="0" y="1412" width="1194" height="86" fill="var(--brown)"/>
    <rect x="0" y="1498" width="598" height="130" fill="var(--white)"/>
    <rect x="598" y="1498" width="596" height="130" fill="var(--blue-light)"/>
  </svg>

  <div class="abs brand-name">Hollowbrook Rails</div>
  <div class="abs brand-phone">555-301-2874</div>
  <div class="abs brand-tag">"Because Good Fences Make Good Neighbors"</div>

  <h1 class="abs headline">WE BUILD<br>FENCES....</h1>
  <p class="abs subhead">AND WE WOULD<br>LOVE TO BUILD YOUR<br>FENCE TOO!</p>

  <h2 class="abs why">WHY<span>CHOOSE US?</span></h2>
  <div class="abs why-rule"></div>
  <p class="abs why-lead">Beautiful, professionally installed fences at affordable prices!</p>
  <ul class="abs perks">
    <li><svg viewBox="0 0 20 20"><path d="M3 10l5 5 9-10" fill="none" stroke="#f7941d" stroke-width="3"/></svg>Free Estimates</li>
    <li><svg viewBox="0 0 20 20"><path d="M3 10l5 5 9-10" fill="none" stroke="#f7941d" stroke-width="3"/></svg>Professional Installation</li>
    <li><svg viewBox="0 0 20 20"><path d="M3 10l5 5 9-10" fill="none" stroke="#f7941d" stroke-width="3"/></svg>Concrete in EVERY Post</li>
    <li><svg viewBox="0 0 20 20"><path d="M3 10l5 5 9-10" fill="none" stroke="#f7941d" stroke-width="3"/></svg>HOA Submission Assistance</li>
    <li><svg viewBox="0 0 20 20"><path d="M3 10l5 5 9-10" fill="none" stroke="#f7941d" stroke-width="3"/></svg>Lifetime Workmanship Warranty</li>
    <li><svg viewBox="0 0 20 20"><path d="M3 10l5 5 9-10" fill="none" stroke="#f7941d" stroke-width="3"/></svg>Experienced Installation Teams</li>
    <li><svg viewBox="0 0 20 20"><path d="M3 10l5 5 9-10" fill="none" stroke="#f7941d" stroke-width="3"/></svg>Quality Workmanship &amp; Materials</li>
    <li><svg viewBox="0 0 20 20"><path d="M3 10l5 5 9-10" fill="none" stroke="#f7941d" stroke-width="3"/></svg>FREE Gate Adjustments for LIFE</li>
  </ul>

  <div class="abs where">WHERE ARE WE?</div>
  <div class="abs address">418 Millbrook Rd<br>Braxton, NC 28099</div>
  <div class="abs showroom">Visit our indoor &amp; outdoor showroom!</div>

  <div class="abs web">www.mybraxtonyard.com</div>
  <p class="abs hours">Our outdoor showroom is open 24/7, while our indoor showroom and <b>office is open Monday - Thurs 9AM - 3PM, Friday 9AM - 1PM</b></p>
</div>
</body>
</html>
```